Design a Retail Box for Industrial Welding Helmets

We are excited to launch a design contest for our product's new retail packaging.
The products are 2 welding helmets.
Product 1 is Valdoran helmet and product 2 is Strelka helmet.
We are seeking for :
A) 1 main design of the box with minor adjustments for the 2 different models (Valdoran and Strelka)
B) 1 design for the sticker of Valdoran (font)
C)1 design for the sticker of Strelka (font)
Attached you will find:
1)Brand logo
2)Reference of welding wire packaging
3)Reference of welding torch packaging
4)Photo of Valdoran model
5)Data of Valdoran model to be included
6)Photo of Strelka model
7)Data of Strelka model to be included
8)Dieline Template of the box in .ai and .jpg
9)Vectors for the different uses of the helmets
Your design should reflect our brand and communicate the product's value while standing out on retail shelves.
The winner will be selected based on creativity, brand alignment, and overall design aesthetics.
We look forward to seeing your creative concepts.
Target Market(s)
Industrial and Retail
Industry/Entity Type
Welding, Retail, Hardware
Colors
Designer to choose colors to be used in the design.
Look and feel
Each slider illustrates characteristics of the customer's brand and the style your logo design should communicate.

```html
<!DOCTYPE html>
<html lang="en">
<head>
<meta charset="utf-8">
<title>Korvan Valdoran Welding Helmet – Box Dieline</title>
<link href="https://fonts.googleapis.com/css2?family=Montserrat:wght@400;600;700;800&display=swap" rel="stylesheet">
<style>
  :root{
    --paper:#ffffff;
    --night:#170a29;
    --violet:#3b1660;
    --plum:#7a2d8f;
    --band:#5e2b8a;
    --glow:#b4459f;
    --tag:#f5a623;
    --ink:#ffffff;
    --cut:#e8322b;
    --fold:#1fa31f;
    --photo-a:#2a2a30;
    --photo-b:#0d0d10;
  }
  *{box-sizing:border-box;margin:0;padding:0}
  html,body{width:1200px;height:965px;overflow:hidden;background:var(--paper)}
  body{position:relative;font-family:"Montserrat",sans-serif;color:var(--ink)}

  .panel{position:absolute;overflow:hidden;
    background:
      radial-gradient(ellipse 60% 45% at 50% 40%, rgba(180,69,159,.45), transparent 70%),
      linear-gradient(180deg,#21103a 0%,var(--violet) 45%,var(--night) 100%);}
  .panel--front{width:271px;height:357px;top:449px}
  .panel--side{width:249px;height:357px;top:449px}

  .brand{position:absolute;left:0;top:26px;font-weight:800;font-size:15px;letter-spacing:1px;display:flex;align-items:center;gap:5px}
  .brand__dot{width:7px;height:7px;border-radius:50%;background:var(--ink)}
  .panel--front .brand{left:20px}
  .panel--side .brand{left:20px}

  .features{position:absolute;left:10px;top:89px;width:83px}
  .feature{position:relative;height:26px;margin-bottom:10.5px;border:1px solid var(--ink);border-radius:3px;
    display:flex;align-items:center;padding:0 3px 0 4px;gap:4px}
  .feature__icon{flex:none;width:13px;height:13px;border:1.4px solid var(--ink);border-radius:50%}
  .feature__text{flex:1;font-size:4.6px;line-height:1.25;text-align:right}
  .feature__tag{position:absolute;right:3px;bottom:-4px;background:var(--tag);color:var(--ink);font-size:4.6px;font-weight:600;padding:0 2px;line-height:7px}

  .product-photo{position:absolute;left:121px;top:47px;width:137px;height:190px;border-radius:45% 40% 35% 40%;
    background:radial-gradient(ellipse at 40% 35%,var(--photo-a),var(--photo-b))}

  .title{position:absolute;left:20px;top:243px}
  .title__brand{font-weight:700;font-size:21px;letter-spacing:2px;line-height:1}
  .title__model{font-weight:600;font-size:36px;line-height:1;letter-spacing:.5px;color:transparent;-webkit-text-stroke:1px var(--ink);margin-top:2px;margin-left:-6px}
  .title__type{font-weight:700;font-size:14.5px;line-height:1;margin-left:78px;margin-top:1px}

  .band{position:absolute;left:0;right:0;bottom:0;height:25px;background:var(--band);display:flex;align-items:center;padding:0 4px}
  .band__slogan{font-weight:700;font-size:9.5px;flex:1}
  .band__uses{display:flex;gap:6px}
  .use{width:16px;height:16px;background:var(--paper);border-radius:1px;color:#111;font-size:3.3px;font-weight:800;text-align:center;padding-top:1px}
  .panel--side .band__uses{margin-right:-2px}

  .flap-top{position:absolute;left:95px;top:203px;width:271px;height:246px;transform:rotate(180deg)}
  .flap-top .brand{left:206px;top:14px;font-size:11px}
  .flap-top .features{left:12px;top:62px;width:53px;right:auto}
  .flap-top .feature{height:16px;margin-bottom:7px;gap:2px}
  .flap-top .feature__icon{width:8px;height:8px;border-width:1px}
  .flap-top .feature__text{font-size:3px}
  .flap-top .feature__tag{font-size:3px;line-height:5px;bottom:-3px}
  .flap-top .product-photo{left:111px;top:14px;width:118px;height:157px}
  .flap-top .title{left:12px;top:163px}
  .flap-top .title__brand{font-size:16px}
  .flap-top .title__model{font-size:27px}
  .flap-top .title__type{font-size:10.5px;margin-left:58px}
  .flap-top .band{height:10px}
  .flap-top .band__slogan{font-size:7px;flex:none}

  .hang-tab{position:absolute;left:162px;top:175px;width:138px;height:28px;border-radius:12px 12px 0 0;
    background:linear-gradient(180deg,var(--plum),var(--violet))}
  .hang-tab__slot{position:absolute;left:39px;bottom:2px;width:60px;height:4px;background:var(--paper);border-radius:2px}

  .dieline{position:absolute;left:0;top:0;width:1200px;height:965px;pointer-events:none}
  .dieline .cut{fill:none;stroke:var(--cut);stroke-width:.7}
  .dieline .fold{fill:none;stroke:var(--fold);stroke-width:.7}
</style>
</head>
<body>

  <div class="hang-tab"><span class="hang-tab__slot"></span></div>

  <section class="panel flap-top" aria-label="Top flap">
    <div class="brand"><span class="brand__dot"></span>KORVAN</div>
    <div class="features">
      <div class="feature"><span class="feature__icon"></span><span class="feature__text">Simple shift fast/mid/slow from 0.1~0.8s</span><span class="feature__tag">DELAY</span></div>
      <div class="feature"><span class="feature__icon"></span><span class="feature__text">Switches from light to dark in just 1/25000 sec</span><span class="feature__tag">SENSITIVITY</span></div>
      <div class="feature"><span class="feature__icon"></span><span class="feature__text">Easy outside control</span><span class="feature__tag">GRIND</span></div>
      <div class="feature"><span class="feature__icon"></span><span class="feature__text">Self-testing and low battery notice</span><span class="feature__tag">TEST</span></div>
    </div>
    <div class="product-photo" role="img" aria-label="Photo of the black auto-darkening welding helmet"></div>
    <div class="title">
      <div class="title__brand">KORVAN</div>
      <div class="title__model">VALDORAN</div>
      <div class="title__type">WELDING HELMET</div>
    </div>
    <div class="band"><span class="band__slogan">The choice of experts.</span></div>
  </section>

  <section class="panel panel--front" style="left:95px" aria-label="Front panel">
    <div class="brand"><span class="brand__dot"></span>KORVAN</div>
    <div class="features">
      <div class="feature"><span class="feature__icon"></span><span class="feature__text">Simple shift fast/mid/slow from 0.1~0.8s</span><span class="feature__tag">DELAY</span></div>
      <div class="feature"><span class="feature__icon"></span><span class="feature__text">Switches from light to dark in just 1/25000 sec</span><span class="feature__tag">SENSITIVITY</span></div>
      <div class="feature"><span class="feature__icon"></span><span class="feature__text">Easy outside control</span><span class="feature__tag">GRIND</span></div>
      <div class="feature"><span class="feature__icon"></span><span class="feature__text">Self-testing and low battery notice</span><span class="feature__tag">TEST</span></div>
    </div>
    <div class="product-photo" role="img" aria-label="Photo of the black auto-darkening welding helmet"></div>
    <div class="title">
      <div class="title__brand">KORVAN</div>
      <div class="title__model">VALDORAN</div>
      <div class="title__type">WELDING HELMET</div>
    </div>
    <div class="band"><span class="band__slogan">The choice of experts.</span>
      <div class="band__uses"><span class="use">MIG</span><span class="use">TIG</span><span class="use">STICK</span><span class="use">PLASMA</span><span class="use">GRIND</span></div>
    </div>
  </section>

  <section class="panel panel--side" style="left:366px" aria-label="Side panel">
    <div class="brand"><span class="brand__dot"></span>KORVAN</div>
    <div class="band"><span class="band__slogan">The choice of experts.</span>
      <div class="band__uses"><span class="use">MIG</span><span class="use">TIG</span><span class="use">STICK</span><span class="use">PLASMA</span><span class="use">GRIND</span></div>
    </div>
  </section>

  <section class="panel panel--front" style="left:615px" aria-label="Back panel">
    <div class="brand"><span class="brand__dot"></span>KORVAN</div>
    <div class="features">
      <div class="feature"><span class="feature__icon"></span><span class="feature__text">Simple shift fast/mid/slow from 0.1~0.8s</span><span class="feature__tag">DELAY</span></div>
      <div class="feature"><span class="feature__icon"></span><span class="feature__text">Switches from light to dark in just 1/25000 sec</span><span class="feature__tag">SENSITIVITY</span></div>
      <div class="feature"><span class="feature__icon"></span><span class="feature__text">Easy outside control</span><span class="feature__tag">GRIND</span></div>
      <div class="feature"><span class="feature__icon"></span><span class="feature__text">Self-testing and low battery notice</span><span class="feature__tag">TEST</span></div>
    </div>
    <div class="product-photo" role="img" aria-label="Photo of the black auto-darkening welding helmet"></div>
    <div class="title">
      <div class="title__brand">KORVAN</div>
      <div class="title__model">VALDORAN</div>
      <div class="title__type">WELDING HELMET</div>
    </div>
    <div class="band"><span class="band__slogan">The choice of experts.</span>
      <div class="band__uses"><span class="use">MIG</span><span class="use">TIG</span><span class="use">STICK</span><span class="use">PLASMA</span><span class="use">GRIND</span></div>
    </div>
  </section>

  <section class="panel panel--side" style="left:886px;width:250px" aria-label="Side panel">
    <div class="brand"><span class="brand__dot"></span>KORVAN</div>
    <div class="band"><span class="band__slogan">The choice of experts.</span>
      <div class="band__uses"><span class="use">MIG</span><span class="use">TIG</span><span class="use">STICK</span><span class="use">PLASMA</span><span class="use">GRIND</span></div>
    </div>
  </section>

  <svg class="dieline" viewBox="0 0 1200 965" aria-hidden="true">
    <path class="fold" d="M95,449 H1136 M366,449 V806 M615,449 V806 M886,449 V806 M95,449 V806 H1136 V449"/>
    <path class="cut" d="M95,452 L67,459 L67,800 L95,806"/>
    <path class="cut" d="M370,449 L382,402 Q385,393 395,393 L590,393 Q600,393 603,402 L612,449"/>
    <path class="cut" d="M617,449 L628,402 Q631,393 641,393 L866,393 Q876,393 879,402 L885,449"/>
    <path class="cut" d="M722,445 V428 Q722,421 730,421 H772 Q779,421 779,428 V445"/>
    <path class="fold" d="M722,445 V476 H779 V445"/>
    <path class="cut" d="M680,447 H722 M779,447 H820"/>
    <path class="cut" d="M889,449 L901,402 Q904,393 914,393 L1110,393 Q1120,393 1123,402 L1134,449"/>
    <path class="cut" d="M96,806 L160,925 L160,945 Q160,955 170,955 L292,955 Q302,955 302,945 L302,925 L365,806"/>
    <path class="cut" d="M368,806 L368,913 L493,913 Q505,913 500,900 L488,870 L615,806"/>
    <path class="cut" d="M617,806 L617,955 L672,955 Q682,955 680,945 L678,927 L822,927 L820,945 Q818,955 828,955 L885,955 L885,806"/>
    <path class="cut" d="M888,806 L1012,868 L1000,900 Q996,913 1010,913 L1133,913 L1136,806"/>
  </svg>

</body>
</html>
```